ONE PAGE WEB DESIGN NEEDED for Finance Company

We need a web design (ONE PAGE DESIGN ONLY) for a new finance website called Brightwell Lending. Brightwell Lending helps customers get the right loan, whether its a home loan, investment loan, business loan etc.

You are required to come up with just the homepage design. Professionalism and quality is the key factors in the successful design.

Here are a few design questions to help you out:

-
What information should be used on the page?
Ive provided a document which outlines all the information needed to put on homepage (attached to the brief - called brightwell_page_info). Also see the Must Have section below on this brief.

-
What links should appear in the navigation/footer?:
The navigation should provide links to the following pages (NOTE: services link has subcategories):
1 Homepage
2 Services
- Home loans
- Investment loans
- Refinancing loans
- Business loans
3 About Us
4 FAQ
5 Contact Us

-
What colors should be used in the design?
Our company colors - Cyan: #2EADE3, Blue: #004B70, White. Feel free to submit designs with slight variations if you feel it improves the design.

-
What should the layout of the page be?
This is up to you to come up with - we are open to different layouts for the page design (as long as they capture the information effectively and making it easy to understand).

Target Market(s)

Potential Home owners, Families and Business Owners

Industry/Entity Type

Business

Requirements
Must have
• - Must contain our logo (attached as PNG and Illustrator file)
- Winning designer must supply a Photoshop file (PSD) that will allow us.
Nice to have
• - Should include photos/images of families, professional groups, tradespeople etc (you can use stock photos from PixQuarry and I will purchase them once you are selected as the winning design)
- Link to a loan calculator somewhere on front page with a button 'Find out how much you could borrow' (or maybe even try adding a loan calculator to the homepage if you think this would look good)
- Page should have a main headline "Finding the right loan for you" or "Brightwell Lending finds the right loan for our customers."
- Must include Accreditation logos somewhere on the homepage (will try and supply these soon)
Should not have
• - Poor quality designs will not be considered
- Do not use clipart

```html
<!DOCTYPE html>
<html lang="en">
<head>
<meta charset="utf-8">
<title>Brightwell Lending – Finding the right loan for you</title>
<link rel="stylesheet" href="https://fonts.googleapis.com/css2?family=Arimo:wght@400;700&family=PT+Sans:wght@400;700&family=Noto+Serif:ital,wght@1,400;1,700&display=swap">
<style>
  :root {
    --page-bg: #e7e5e0;
    --page-bg-light: #efeeea;
    --brand-blue: #004b70;
    --brand-cyan: #2eade3;
    --nav-ink: #1d3c55;
    --menu-bg: #102a3c;
    --menu-current: #6cc0ef;
    --heading-ink: #333333;
    --body-ink: #555555;
    --frame: #d6d3cd;
    --frame-edge: #c7c4be;
    --button: #5aa8e2;
    --button-dark: #4596d2;
    --footer-bg: #2a2a2a;
    --footer-ink: #c9c9c9;
    --footer-faint: #4d4d4d;
    --white: #ffffff;
  }
  * { box-sizing: border-box; margin: 0; padding: 0; }
  html, body { width: 903px; height: 1200px; overflow: hidden; }
  body {
    position: relative;
    background: radial-gradient(ellipse at 50% 35%, var(--page-bg-light), var(--page-bg) 70%);
    font-family: "Arimo", Arial, sans-serif;
    color: var(--body-ink);
  }
  .abs { position: absolute; }

  /* Brand */
  .brand-mark {
    left: 427px; top: 36px; width: 40px; height: 40px;
    border-radius: 50%; border: 4px solid var(--brand-blue);
  }
  .brand-name {
    left: 0; width: 903px; top: 90px; text-align: center;
    font-family: "PT Sans", sans-serif; font-weight: 700;
    font-size: 23px; color: var(--brand-blue);
  }
  .tagline {
    left: 0; width: 903px; top: 120px; text-align: center;
    font-family: "Noto Serif", serif; font-style: italic;
    font-size: 10.5px; color: var(--nav-ink);
  }

  /* Navigation */
  .main-nav { top: 148px; left: 0; width: 903px; height: 20px; }
  .main-nav a {
    position: absolute; top: 0; height: 20px; line-height: 20px;
    font-family: "PT Sans", sans-serif; font-size: 11px;
    color: var(--nav-ink); text-decoration: none;
  }
  .main-nav .is-active {
    padding: 0 6px; border: 1px solid #cfccc6; border-radius: 4px;
    background: linear-gradient(#f4f3f0, #e2e0db); line-height: 18px;
  }
  .dropdown {
    z-index: 10;
    background: var(--menu-bg); border-radius: 3px;
    box-shadow: 0 2px 4px rgba(0,0,0,.3);
    list-style: none;
  }
  .dropdown li {
    font-family: "Noto Serif", serif; font-style: italic;
    font-size: 8.5px; line-height: 16px; color: var(--white);
    white-space: nowrap;
  }
  .dropdown li.current { color: var(--menu-current); }
  .services-menu { left: 368px; top: 179px; width: 84px; padding: 9px 8px 10px; }
  .services-menu::before {
    content: ""; position: absolute; top: -6px; left: 9px;
    border: 6px solid transparent; border-top: 0; border-bottom-color: var(--menu-bg);
  }

  /* Slider */
  .slider-frame {
    left: 115px; top: 189px; width: 670px; height: 316px;
    background: var(--frame); border: 1px solid var(--frame-edge);
    box-shadow: 0 4px 8px rgba(0,0,0,.12);
  }
  .slider-photo {
    left: 122px; top: 196px; width: 657px; height: 304px;
    background: linear-gradient(180deg, #7d8f6a 0%, #b9a99a 45%, #d6b9ad 75%, #a58c76 100%);
  }
  .slider-arrow {
    top: 320px; width: 37px; height: 37px; border-radius: 50%;
    background: radial-gradient(circle at 50% 35%, #ffffff, #e1e1df);
    box-shadow: 0 2px 4px rgba(0,0,0,.25);
  }
  .slider-arrow svg { display: block; margin: 9px auto; }
  .arrow-prev { left: 97px; }
  .arrow-next { left: 766px; }

  /* Intro */
  .intro { left: 135px; top: 531px; width: 430px; }
  .intro h1 {
    font-size: 12.5px; font-weight: 700; color: var(--heading-ink);
    letter-spacing: .2px; margin-bottom: 18px;
  }
  .intro p { font-size: 8.8px; line-height: 16px; margin-bottom: 15px; }

  .divider {
    left: 130px; width: 643px; height: 12px;
    background: radial-gradient(ellipse at 50% 0, rgba(0,0,0,.12), transparent 70%);
  }

  /* Loan tiles */
  .tile {
    top: 742px; width: 134px; height: 132px;
    background: var(--frame); border: 1px solid var(--frame-edge);
  }
  .tile-photo { position: absolute; left: 5px; top: 5px; right: 5px; bottom: 5px; }
  .tile-label {
    position: absolute; left: -7px; top: 11px; height: 15px; padding: 0 9px;
    background: var(--menu-bg); color: var(--white);
    font-size: 7.5px; font-weight: 700; line-height: 15px;
  }
  .tile-home { left: 136px; }
  .tile-home .tile-photo { background: linear-gradient(135deg, #6a6a6a, #d8d8d8 60%, #9c9c9c); }
  .tile-invest { left: 302px; }
  .tile-invest .tile-photo { background: linear-gradient(180deg, #5aa2d6, #a9cde6 50%, #7eb04a 75%, #e0b89a); }
  .tile-refi { left: 468px; }
  .tile-refi .tile-photo { background: linear-gradient(135deg, #c8845c, #4f5f80 45%, #b8c0d0 80%); }
  .tile-business { left: 634px; }
  .tile-business .tile-photo { background: linear-gradient(135deg, #3a3c40, #e3e3e3 55%, #6b6e74); }
  .home-menu { left: 147px; top: 779px; min-width: 83px; padding: 6px 7px; }

  .panel-note { left: 135px; top: 941px; width: 425px; font-size: 8.8px; line-height: 16px; }

  .borrow-button {
    left: 295px; top: 1013px; width: 312px; height: 29px;
    background: linear-gradient(var(--button), var(--button-dark));
    border-radius: 2px; box-shadow: 0 2px 3px rgba(0,0,0,.2);
    color: var(--white); font-size: 14.5px; text-align: center; line-height: 29px;
    text-decoration: none;
  }

  /* Footer */
  .site-footer {
    left: 0; top: 1077px; width: 903px; height: 123px;
    background: var(--footer-bg); border-top: 7px solid #363636;
    text-align: center;
  }
  .footer-contact { position: absolute; top: 20px; width: 100%; font-size: 11px; color: var(--footer-ink); }
  .footer-contact strong { color: #e4e4e4; }
  .footer-nav { position: absolute; top: 48px; width: 100%; font-family: "PT Sans", sans-serif; font-size: 10px; color: var(--footer-ink); }
  .footer-nav a, .footer-nav a:visited { color: var(--footer-ink); text-decoration: none; }
  .footer-nav span { margin: 0 9px; }
  .copyright { position: absolute; top: 77px; width: 100%; font-size: 9px; color: var(--footer-faint); }
</style>
</head>
<body>
  <header>
    <div class="abs brand-mark"></div>
    <div class="abs brand-name">Brightwell Lending</div>
    <div class="abs tagline">Finding the right loan for you</div>

    <nav class="abs main-nav">
      <a href="#" style="left:309px">Home</a>
      <a href="#" class="is-active" style="left:356px">Services</a>
      <a href="#" style="left:428px">About us</a>
      <a href="#" style="left:496px">FAQ</a>
      <a href="#" style="left:542px">Contact us</a>
    </nav>
  </header>

  <section>
    <div class="abs slider-frame"></div>
    <div class="abs slider-photo" role="img" aria-label="Photo of a smiling three-generation family sitting together outdoors"></div>
    <a href="#" class="abs slider-arrow arrow-prev" aria-label="Previous slide">
      <svg width="18" height="18" viewBox="0 0 18 18"><path d="M12 2 L5 9 L12 16" fill="none" stroke="#46a6dc" stroke-width="3.5" stroke-linecap="round" stroke-linejoin="round"/></svg>
    </a>
    <a href="#" class="abs slider-arrow arrow-next" aria-label="Next slide">
      <svg width="18" height="18" viewBox="0 0 18 18"><path d="M6 2 L13 9 L6 16" fill="none" stroke="#46a6dc" stroke-width="3.5" stroke-linecap="round" stroke-linejoin="round"/></svg>
    </a>
  </section>

  <ul class="abs dropdown services-menu">
    <li class="current">Home loans</li>
    <li>Investment loans</li>
    <li>Refinancing loans</li>
    <li>Business loans</li>
  </ul>

  <section class="abs intro">
    <h1>BRIGHTWELL LENDING HOME PAGE INFORMATION</h1>
    <p>At Brightwell Lending we work hard to find the right loan for our customers. We do that because we are backed by sound industry knowledge, professional experience and a great customer service approach.</p>
    <p>Brightwell Lending guarantees that we will always tailor the best solution for your individual lending needs.</p>
    <p>We can do that because we have access to a wide variety of lending options from major banks to non-bank lenders and we are committed to finding the right lending product for you.</p>
  </section>

  <div class="abs divider" style="top:705px"></div>

  <section>
    <div class="abs tile tile-home">
      <div class="tile-photo" role="img" aria-label="Photo of a model house resting on loan paperwork"></div>
      <span class="tile-label">Home Loan</span>
    </div>
    <div class="abs tile tile-invest">
      <div class="tile-photo" role="img" aria-label="Photo of cupped hands holding coins with a young plant growing"></div>
      <span class="tile-label">Investment Loan</span>
    </div>
    <div class="abs tile tile-refi">
      <div class="tile-photo" role="img" aria-label="Photo of a fanned-out stack of banknotes"></div>
      <span class="tile-label">Refinancing</span>
    </div>
    <div class="abs tile tile-business">
      <div class="tile-photo" role="img" aria-label="Photo of business people exchanging a document"></div>
      <span class="tile-label">Business Loan</span>
    </div>
    <ul class="abs dropdown home-menu">
      <li class="current">Home buyers</li>
      <li>First home buyers</li>
      <li>Over 20 lenders</li>
    </ul>
  </section>

  <div class="abs divider" style="top:901px"></div>

  <p class="abs panel-note">There are many different loan products in the marketplace. &nbsp;&nbsp;&nbsp;&nbsp;&nbsp;Brightwell Lending has access to a wide panel of lenders which means we can access bank and non-bank lenders that meet the individual needs of our customers.</p>

  <a href="#" class="abs borrow-button">Find out how much you could borrow</a>

  <footer class="abs site-footer">
    <p class="footer-contact">Contact Brightwell Lending today on: <strong>1800 555 012</strong> to find out more.</p>
    <nav class="footer-nav">
      <a href="#">Home</a><span>|</span><a href="#">Services</a><span>|</span><a href="#">About</a><span>|</span><a href="#">FAQ</a><span>|</span><a href="#">Contact us</a>
    </nav>
    <p class="copyright">© Copyright 2012.</p>
  </footer>
</body>
</html>
```